Awesome photographers card for an awesome new business

Double sided business card Black background and silver logo in middle on one side. Details on otherside. please keep it simple

Photographer

Gavin Tolley
0482615073
GavinTolleyPhotography82@lumenpost.com
www.GavinTolleyPhotography.com.au
Instagram _Gavin_tolley

Requirements
Must have
• My logo in Silver
• please use instagram logo instead of "Instagram"

```html
<!DOCTYPE html>
<html lang="en">
<head>
<meta charset="utf-8">
<title>Gavin Tolley Photography – Business Card</title>
<link href="https://fonts.googleapis.com/css2?family=Roboto:wght@400;500&family=Roboto+Condensed:wght@500&display=swap" rel="stylesheet">
<style>
  :root {
    --backdrop: #1c1c1c;
    --card-front: #f3f3f3;
    --ink: #5a5a5a;
    --ink-soft: #626262;
    --mark-front: #7a7a7a;
    --mark-back: #f2f2f2;
    --divider: #b9b9b9;
    --band-dark: #6e6e6e;
    --band-light: #bdbdbd;
    --silver-edge: #8a8a8a;
    --silver-mid: #c4c4c4;
    --url-back: #ffffff;
  }
  * { margin: 0; padding: 0; box-sizing: border-box; }
  html, body { width: 1200px; height: 960px; overflow: hidden; }
  body {
    background: var(--backdrop);
    font-family: "Roboto", Arial, sans-serif;
    position: relative;
  }
  .card {
    position: absolute;
    width: 600px;
    height: 342px;
    box-shadow: 0 4px 10px rgba(0,0,0,.5);
    overflow: hidden;
  }
  .card--front { left: 314px; top: 113px; background: var(--card-front); }
  .card--back {
    left: 311px; top: 472px; height: 343px;
    background: linear-gradient(90deg, var(--silver-edge) 0%, var(--silver-mid) 50%, var(--silver-edge) 100%);
  }
  .brand-mark {
    position: absolute;
    border-radius: 50%;
    display: flex;
    align-items: center;
    justify-content: center;
    text-align: center;
    font-family: "Roboto", Arial, sans-serif;
    font-weight: 500;
    letter-spacing: 2px;
    text-transform: uppercase;
  }
  .card--front .brand-mark {
    left: 50px; top: 96px; width: 150px; height: 150px;
    border: 3px solid var(--mark-front);
    color: var(--mark-front);
    font-size: 15px;
    line-height: 1.4;
  }
  .card--back .brand-mark {
    left: 221px; top: 91px; width: 160px; height: 160px;
    border: 3px solid var(--mark-back);
    color: var(--mark-back);
    font-size: 16px;
    line-height: 1.4;
  }
  .divider {
    position: absolute;
    left: 224px; top: 106px;
    width: 2px; height: 134px;
    background: var(--divider);
  }
  .owner-name {
    position: absolute;
    left: 244px; top: 113px;
    font-family: "Roboto Condensed", "Arial Narrow", sans-serif;
    font-weight: 500;
    font-size: 21px;
    color: var(--ink);
    text-transform: uppercase;
  }
  .contact-list {
    position: absolute;
    left: 244px; top: 156px;
    list-style: none;
  }
  .contact-list li {
    display: flex;
    align-items: center;
    height: 19px;
    font-size: 14.5px;
    color: var(--ink-soft);
  }
  .contact-list svg { width: 13px; height: 13px; margin-right: 13px; flex: none; fill: var(--ink); }
  .base-band { position: absolute; left: 0; bottom: 0; width: 600px; height: 13px; }
  .back-url {
    position: absolute;
    left: 0; right: 0; top: 292px;
    text-align: center;
    font-size: 14px;
    letter-spacing: 2.2px;
    color: var(--url-back);
  }
</style>
</head>
<body>
  <section class="card card--front">
    <div class="brand-mark">Gavin<br>Tolley</div>
    <div class="divider"></div>
    <h1 class="owner-name">Gavin Tolley</h1>
    <ul class="contact-list">
      <li>
        <svg viewBox="0 0 16 16"><path d="M3.6 1.2l2.3 2.8-1.3 1.8c.9 2 2.4 3.5 4.4 4.4l1.8-1.3 2.8 2.3-1.3 2.3C7 15.3.7 9 1.3 2.5z"/></svg>
        0482615073
      </li>
      <li>
        <svg viewBox="0 0 16 16"><path d="M1 3h14v10H1z M2 4.5v.6l6 4 6-4v-.6z" fill-rule="evenodd"/></svg>
        GavinTolleyPhotography82@lumenpost.com
      </li>
      <li>
        <svg viewBox="0 0 16 16"><circle cx="8" cy="8" r="7"/><path d="M1 8h14M8 1c-2.5 2-2.5 12 0 14M8 1c2.5 2 2.5 12 0 14" stroke="#f3f3f3" stroke-width="1.2" fill="none"/></svg>
        www.GavinTolleyPhotography.com.au
      </li>
      <li>
        <svg viewBox="0 0 16 16"><rect x="1" y="1" width="14" height="14" rx="2"/></svg>
        Gavin_tolley
      </li>
    </ul>
    <svg class="base-band" viewBox="0 0 600 13" preserveAspectRatio="none">
      <defs>
        <linearGradient id="bandDark" x1="0" x2="1">
          <stop offset="0" stop-color="#5e5e5e"/><stop offset=".6" stop-color="#8d8d8d"/><stop offset="1" stop-color="#6a6a6a"/>
        </linearGradient>
      </defs>
      <rect width="600" height="13" fill="var(--band-light)"/>
      <polygon points="0,0 394,0 389,13 0,13" fill="url(#bandDark)"/>
      <polygon points="394,0 398,0 393,13 389,13" fill="#ffffff"/>
    </svg>
  </section>

  <section class="card card--back">
    <div class="brand-mark">Gavin<br>Tolley</div>
    <p class="back-url">www.GavinTolleyPhotography.com.au</p>
  </section>
</body>
</html>
```